Tallbrook Meridian Advisory needs business cards

Tallbrook Meridian Advisory is a new approach to consulting: we believe in partnering our clients in a hands-on, side-by-side, rolling-up-our sleeves approach, rather than being removed and aloof consultants.

We have a logo design developped through PixelHarbor (see attachment) and need to move to the stage of designing a business card for our 7 founding members.

Target Market(s)

Senior executives in local and global companies (such as Fizzmont Tonic, Hollanby, Brevard, etc)

Industry/Entity Type

Business

Requirements
Must have
• Look and feel: The design reflect the logo: i.e. professional, modern and approachable (as opposed to corporate traditional and remote). We are looking for a high quality, premium design.

Content must haves:
- prominent: our logo, person's name, function, phone number and e-mail address
- less prominent: company address and website

Example: Tallbrook Meridian Advisory logo, Mireille Vostag, Partner, +44 (0)781 209 3375, mireille_vostag@tallbrookmeridian.example / 17 Pelham Crescent, Esher, Surrey, UK, KT10 3WN - www.tallbrookmeridian.example

- Both sides of the card can be used
- Both versions of the logo can be used (on black or on white)

```html
<!DOCTYPE html>
<html lang="en">
<head>
<meta charset="utf-8">
<title>Tallbrook Meridian Advisory — Business Cards</title>
<link rel="stylesheet" href="https://fonts.googleapis.com/css2?family=Open+Sans:wght@400;600;700&display=swap">
<style>
  :root {
    --stage: #b08a2c;
    --brand-blue: #1596d8;
    --brand-blue-deep: #0b5fa0;
    --brand-blue-light: #5cc4ee;
    --ink: #2a2a2a;
    --ink-soft: #3c3c3c;
    --card-white: #ffffff;
    --band-grey: #e7e7e7;
    --card-black: #000000;
  }
  * { margin: 0; padding: 0; box-sizing: border-box; }
  html, body {
    width: 1200px; height: 686px; overflow: hidden;
    background: var(--stage);
    font-family: "Open Sans", Arial, sans-serif;
  }
  .canvas { position: relative; width: 1200px; height: 686px; }

  .card {
    position: absolute; width: 463px; height: 264px;
    border-radius: 20px; overflow: hidden;
    box-shadow: 0 2px 4px rgba(0,0,0,0.35);
  }

  /* Front */
  .card-front { left: 123px; top: 102px; background: var(--card-white); }
  .front-band { position: absolute; left: 0; top: 0; width: 463px; height: 264px; }
  .front-edge {
    position: absolute; right: 0; top: 0; width: 23px; height: 264px;
    background: linear-gradient(180deg, var(--brand-blue-deep) 0%, var(--brand-blue) 45%, var(--brand-blue-light) 70%, var(--brand-blue-deep) 100%);
    border-left: 1px solid #0a3f6e;
  }
  .brand {
    position: absolute; left: 66px; top: 44px; width: 340px;
    display: flex; align-items: center; gap: 14px;
  }
  .brand-dot {
    flex: none; width: 64px; height: 64px; border-radius: 50%;
    background: var(--brand-blue);
  }
  .brand-name {
    font-weight: 700; font-size: 25px; line-height: 1.08;
    color: var(--ink); letter-spacing: -0.3px;
  }
  .contact {
    position: absolute; left: 0; width: 440px; text-align: center;
  }
  .person { top: 162px; font-size: 17px; font-weight: 700; color: var(--brand-blue); }
  .person .role { font-size: 12.5px; color: var(--ink); }
  .lines { top: 193px; font-size: 11.3px; color: var(--ink-soft); line-height: 18px; }
  .lines .row { display: flex; justify-content: center; align-items: center; gap: 10px; }
  .lines .item { display: inline-flex; align-items: center; gap: 3px; }
  .lines svg { width: 10px; height: 10px; fill: var(--brand-blue); }
  .web {
    top: 229px; font-size: 11.5px; font-weight: 700; letter-spacing: 1.4px; color: var(--ink);
  }
  .web .accent { color: var(--brand-blue); }

  /* Back */
  .card-back {
    left: 605px; top: 371px;
    background: radial-gradient(ellipse 55% 70% at 50% 40%, #2a2a2a 0%, #0d0d0d 55%, var(--card-black) 100%);
  }
  .back-floor { position: absolute; left: 0; top: 0; width: 463px; height: 264px; }
  .back-brand {
    position: absolute; left: 0; top: 62px; width: 463px;
    display: flex; flex-direction: column; align-items: center; gap: 12px;
  }
  .back-brand .brand-dot { width: 72px; height: 72px; }
  .back-brand .brand-name { color: #ffffff; font-size: 20px; }
</style>
</head>
<body>
<main class="canvas">

  <section class="card card-front" aria-label="Business card, front">
    <svg class="front-band" viewBox="0 0 463 264" aria-hidden="true">
      <defs>
        <linearGradient id="bandFade" x1="0" y1="0" x2="0" y2="1">
          <stop offset="0" stop-color="#e4e4e4"/>
          <stop offset="1" stop-color="#fbfbfb"/>
        </linearGradient>
      </defs>
      <path d="M0 182 Q220 95 463 165 L463 264 L0 264 Z" fill="url(#bandFade)"/>
    </svg>
    <div class="front-edge"></div>

    <div class="brand">
      <span class="brand-dot"></span>
      <span class="brand-name">Tallbrook Meridian<br>Advisory</span>
    </div>

    <p class="contact person">Mireille Vostag<span class="role">, Partner</span></p>
    <div class="contact lines">
      <div class="row">
        <span class="item">
          <svg viewBox="0 0 10 10" aria-hidden="true"><path d="M2 0.5 L3.6 2.6 L2.7 3.6 Q3.8 5.9 6.2 7.2 L7.2 6.3 L9.4 7.9 L8.2 9.5 Q2.6 8.6 0.5 1.8 Z"/></svg>+44 (0)781 209 3375
        </span>
        <span class="item">
          <svg viewBox="0 0 10 10" aria-hidden="true"><path d="M0 2 H10 V8.5 H0 Z M0.6 2.4 L5 5.6 L9.4 2.4" /><path d="M0 2 L5 5.4 L10 2" fill="none" stroke="#fff" stroke-width="0.8"/></svg>mireille_vostag@tallbrookmeridian.example
        </span>
      </div>
      <div class="row">17 Pelham Crescent, Esher, Surrey, UK, KT10 3WN</div>
    </div>
    <p class="contact web">www.<span class="accent">tallbrookmeridian</span>.example</p>
  </section>

  <section class="card card-back" aria-label="Business card, back">
    <svg class="back-floor" viewBox="0 0 463 264" aria-hidden="true">
      <defs>
        <linearGradient id="floorShine" x1="0" y1="0" x2="0" y2="1">
          <stop offset="0" stop-color="#3a3a3a"/>
          <stop offset="0.4" stop-color="#141414"/>
          <stop offset="1" stop-color="#000"/>
        </linearGradient>
      </defs>
      <path d="M0 222 Q231 140 463 222 L463 264 L0 264 Z" fill="url(#floorShine)"/>
    </svg>
    <div class="back-brand">
      <span class="brand-dot"></span>
      <span class="brand-name">Tallbrook Meridian Advisory</span>
    </div>
  </section>

</main>
</body>
</html>
```